Running Book Cover Design Project

My client has written a book about running and his accomplishments throughout the sport, his story etc. We need to get a cover designed for it. The book will be offered online only, but may later on look at printing a few copies later down the track, so it will need to be a vector graphic so we can resize it easily.

The title of the book is 'Beyond The Far Hill', written by Marco Tevin Alcaraza from the Philippines.

The idea that we have had for the cover is as follows... We would like the word 'step' so be somehow presented in a step, maybe we could use the shoe tread somehow with the word step in it, or use a step in some way, I will leave it up to you, we are pretty open.

Just think that finding running has changed his life and he wants that represented on the cover somehow with the title standing for both taking one more step with running and a metaphor for life.

Do note that the illustration of the 'foot step' has to be a mid-foot or forefoot landing on the ground instead of a heel strike. Reason being that heel strikes can lead to a lot of injuries; the author is against it as well.

UPDATE: The design should have the runner in summer clothes, with bold fonts, not running up steps as these are marathon type events he is running (attached a new image for inspiration), he should be wearing shoes and clothing similar to the attached images from Talvex
Updates

Changes:

AUTHOR - Colin Barr

Sorry about the inclusion of Marco, the author's name should be represented as Colin Barr

Still waiting on final approval, apologies!

Target Market(s)

Adults based in south east asia predominantly singapore and the philippines.

Targeted to all those who enjoy inspirational stories or books about running

Industry/Entity Type

Printing

Requirements
Must have
• Running imagery
Shoe/Step IIllustration
Title of Book
Author's Name

```html
<!DOCTYPE html>
<html lang="en">
<head>
<meta charset="utf-8">
<title>Beyond The Far Hill — Colin Barr</title>
<link href="https://fonts.googleapis.com/css2?family=Roboto+Condensed:wght@400;700&family=Roboto:wght@300&display=swap" rel="stylesheet">
<style>
  :root {
    --white: #ffffff;
    --ground-light: #d9dde2;
    --ground-mid: #aeb3ba;
    --ground-dark: #7f858d;
    --stripe-red: #e2231a;
    --stripe-green: #1f9a3a;
    --stripe-blue: #2f66d0;
    --shorts-red: #e8432a;
    --shorts-green: #3fae3a;
    --shirt-blue: #2c56c8;
    --skin-dark: #4a2f26;
  }
  html, body {
    margin: 0;
    padding: 0;
    width: 900px;
    height: 1200px;
    overflow: hidden;
    background: var(--white);
  }
  .cover {
    position: relative;
    width: 900px;
    height: 1200px;
    overflow: hidden;
    background: linear-gradient(180deg, var(--ground-light) 0%, var(--ground-mid) 70%, var(--ground-dark) 100%);
  }
  .runners-photo {
    position: absolute;
    left: 0;
    top: 0;
    width: 900px;
    height: 760px;
    background:
      linear-gradient(180deg, rgba(0,0,0,0) 70%, rgba(190,196,203,1) 100%),
      linear-gradient(90deg,
        #8fb04a 0%, var(--shorts-red) 14%, var(--skin-dark) 24%,
        var(--shirt-blue) 40%, var(--shorts-green) 52%, var(--skin-dark) 62%,
        var(--shorts-red) 72%, #b9c27a 84%, var(--shirt-blue) 100%);
  }
  .author {
    position: absolute;
    top: 200px;
    left: 0;
    width: 900px;
    text-align: center;
    font-family: "Roboto", sans-serif;
    font-weight: 300;
    font-size: 66px;
    line-height: 80px;
    letter-spacing: 7px;
    color: var(--white);
    margin: 0;
  }
  .title {
    position: absolute;
    top: 740px;
    left: 0;
    width: 900px;
    text-align: center;
    margin: 0;
    font-family: "Roboto Condensed", sans-serif;
    font-weight: 700;
    font-size: 165px;
    line-height: 190px;
    letter-spacing: -3px;
    color: var(--white);
  }
  .title-line {
    display: block;
    white-space: nowrap;
  }
  .colour-bar {
    position: absolute;
    left: 0;
    bottom: 0;
    width: 900px;
    height: 30px;
    display: flex;
  }
  .colour-bar span { display: block; height: 100%; }
  .colour-bar .red { width: 132px; background: var(--stripe-red); }
  .colour-bar .green { width: 412px; background: var(--stripe-green); }
  .colour-bar .blue { flex: 1; background: var(--stripe-blue); }
</style>
</head>
<body>
  <main class="cover">
    <div class="runners-photo" role="img" aria-label="Close-up of marathon runners' legs and colourful running shoes in motion on a road"></div>
    <p class="author">COLIN BARR</p>
    <h1 class="title">
      <span class="title-line">Beyond The</span>
      <span class="title-line">Far Hill</span>
    </h1>
    <div class="colour-bar" aria-hidden="true">
      <span class="red"></span><span class="green"></span><span class="blue"></span>
    </div>
  </main>
</body>
</html>
```